Small Graphic design business needs a marketing flyer

A small graphic design business called Heron Graphics needs an uplift with a trendy, catchy and creative A5 marketing flyer to promote their services. Their services include all aspects of graphic design from corporate branding to brochures, business cards and annual reports, and will take their clients right through to the final printed product.
Logo colours are shades of dark green to lime green, grey and black - see attached. We would like to see some of those colours carried through the design in some way, but not a necessity. The overall feel of the flyer to be eye-catching and enticing, clever, fun and bold to attract customers.

Company logo and some images attached.

Target Market(s)

Anyone who wants to promote their business.

Industry/Entity Type

Graphic Design

Requirements
Must have
• • Must be A5 size
• Include this bit of text:
'Whether it’s a creative logo design, business stationery, ads, brochures, or even typesetting you're after, Heron Graphics can cater to all your design as well as printing needs. We will take you through from beginning to end, from creative design solutions, to the final printed product. We’re here to make things easy for you...to take your business to the next level.

• As far as other wording/heading goes to promote the business, I will leave it to your creativity but must include the promotion stating: 'Mention this flyer to receive 20% off all artwork and 10% off all printing.'

• Contact details to be included too:
Phone (08) 7315 4097
Email: heron.graphics@plovermail.net.au

• Please also include the logo and images (showing some samples of the companies work) attached.

Nice to have
• Would be nice to have some kind of promotion on the flyer e.g. 'if you mention this flyer you will receive 20% off....' or something to that effect.

```html
<!DOCTYPE html>
<html lang="en">
<head>
<meta charset="utf-8">
<title>Heron Graphics – Flyer</title>
<link rel="stylesheet" href="https://fonts.googleapis.com/css2?family=Kumbh+Sans:wght@700&family=Roboto+Condensed:wght@300;400;700&family=Saira:wght@400&family=Roboto:wght@400;700&display=swap">
<style>
:root{
  --page:#ffffff;
  --lime:#a9d37a;
  --lime-soft:#d9ecc4;
  --frame-green:#5a9a2f;
  --ink:#231f20;
  --grey-band:#d6d7d8;
  --navy:#1d2f55;
  --orange:#f08a1c;
  --sky:#3aaed8;
  --brand-green:#4a9a2c;
}
*{margin:0;padding:0;box-sizing:border-box}
html,body{width:1200px;height:900px;overflow:hidden;background:var(--page)}
.canvas{position:relative;width:1200px;height:900px}
.flyer{
  position:absolute;left:305px;top:42px;width:561px;height:796px;
  background:linear-gradient(180deg,var(--lime) 0%,#bfe09b 30%,var(--lime-soft) 55%,#ffffff 80%);
  border:1px solid #8a8a8a;
  box-shadow:6px 8px 10px rgba(0,0,0,.35);
  overflow:hidden;
  font-family:"Roboto Condensed",sans-serif;color:var(--ink);
}
.headline{
  position:absolute;left:0;top:22px;width:100%;text-align:center;
  font-family:"Kumbh Sans",sans-serif;font-weight:700;font-size:55px;line-height:62px;letter-spacing:-.5px;color:var(--ink);
}
.sample-frame{position:absolute;background:#fff;border:5px solid var(--frame-green)}
.sample-brochure{left:72px;top:161px;width:178px;height:273px}
.sample-cards{left:264px;top:161px;width:248px;height:189px}
.sample-logo{left:269px;top:395px;width:172px;height:30px;display:flex;align-items:center;justify-content:center;overflow:hidden}

/* brochure */
.brochure{position:absolute;left:6px;top:7px;width:157px;height:250px;background:#fff;box-shadow:0 0 2px rgba(0,0,0,.3)}
.brochure-head{height:30px;background:var(--navy);color:#fff;position:relative;font-family:"Roboto",sans-serif}
.brochure-title{position:absolute;left:6px;top:4px;font-size:8.5px;line-height:10px;font-weight:400}
.brochure-brand{position:absolute;right:5px;top:9px;font-size:6px;font-weight:700;color:#fff}
.brochure-photo{height:93px;background:linear-gradient(135deg,#e9ddd0 0%,#cfc1b3 45%,#8e97a8 100%)}
.brochure-band{height:16px;background:linear-gradient(180deg,var(--orange),#f9c98e);font-family:"Roboto",sans-serif;font-size:5.5px;font-weight:700;color:var(--navy);padding:5px 0 0 6px}
.brochure-body{display:flex;gap:6px;padding:4px 6px;height:95px;background:linear-gradient(180deg,#fde9d3,#fff 40%)}
.brochure-col{flex:1;font-family:"Roboto",sans-serif;font-size:3.3px;line-height:6px;color:#555}
.brochure-foot{position:absolute;left:0;bottom:0;width:100%;height:16px;background:var(--navy);color:#c9d0de;font-family:"Roboto",sans-serif;font-size:3.5px;display:flex;justify-content:space-around;align-items:center}

/* business cards */
.card-front{position:absolute;left:9px;top:9px;width:103px;height:161px;background:#fff;border:1px solid #9b9b9b;font-family:"Roboto",sans-serif;color:#444;padding:12px 0 0 8px}
.card-name{font-size:4.5px;font-weight:700;color:#222;line-height:5.5px}
.card-lines{margin-top:4px;font-size:3.6px;line-height:5.2px;color:#666}
.card-brand{position:absolute;left:8px;bottom:14px;display:flex;align-items:center;gap:3px;font-family:"Roboto Condensed",sans-serif;font-size:8px;font-weight:700;color:var(--brand-green)}
.brand-square{display:inline-block;width:6px;height:6px;background:var(--sky)}
.card-back{position:absolute;left:123px;top:9px;width:100px;height:161px;background:var(--sky);border:4px solid #111;box-shadow:3px 3px 3px rgba(0,0,0,.6)}
.card-back-top{height:63px;background:#fff;border-bottom:3px solid #111;display:flex;flex-direction:column;align-items:center;justify-content:center;gap:2px}
.card-back-brand{font-family:"Roboto Condensed",sans-serif;font-weight:700;font-size:13px;color:var(--brand-green);display:flex;align-items:center;gap:4px}
.card-back-tag{font-family:"Roboto",sans-serif;font-size:4px;color:#666}

.client-name{font-family:"Roboto Condensed",sans-serif;font-weight:700;font-size:9px;line-height:10px;color:var(--ink);letter-spacing:.2px;white-space:nowrap}

.services{position:absolute;left:19px;top:450px;width:520px;font-size:14.2px;line-height:19px;font-weight:400;color:var(--ink)}

.brand{position:absolute;left:0;top:574px;width:100%;text-align:center}
.brand-name{font-family:"Roboto Condensed",sans-serif;font-weight:700;font-size:30px;color:#4d4d4f;letter-spacing:.5px;line-height:32px}
.brand-tag{font-family:"Roboto Condensed",sans-serif;font-size:11px;color:#4d4d4f;margin-left:70px}
.contact{position:absolute;left:0;top:633px;width:100%;text-align:center;font-family:"Roboto",sans-serif;font-weight:700;font-size:13.5px;color:var(--ink);word-spacing:1px}

.promo-rule{position:absolute;left:0;width:100%;height:6px;background:var(--frame-green)}
.promo{position:absolute;left:0;top:672px;width:100%;height:94px;background:linear-gradient(180deg,#e3e4e5,var(--grey-band));text-align:center;font-family:"Saira",sans-serif;font-size:31px;line-height:38px;padding-top:9px;color:var(--ink)}
</style>
</head>
<body>
<div class="canvas">
  <main class="flyer">
    <h1 class="headline">Let us design<br>your next job!</h1>

    <section class="sample-frame sample-brochure" aria-label="Brochure sample">
      <div class="brochure">
        <div class="brochure-head">
          <div class="brochure-title">GROWTH<br>BUILDER</div>
          <div class="brochure-brand">Meridian</div>
        </div>
        <div class="brochure-photo" role="img" aria-label="Photo of a family relaxing together at home"></div>
        <div class="brochure-band">Growth Builder Service Package</div>
        <div class="brochure-body">
          <div class="brochure-col">Regular reviews of your goals and plans<br>Guidance on savings and super funds<br>Clear reports each quarter<br>Options for managed share funds<br>Support with insurance and tax</div>
          <div class="brochure-col">Personal advice meetings<br>Strategy updates each year<br>Access to online tools<br>Help with estate planning</div>
        </div>
        <div class="brochure-foot"><span>Growth Builder</span><span>Solutions</span><span>Advisers</span></div>
      </div>
    </section>

    <section class="sample-frame sample-cards" aria-label="Business card sample">
      <div class="card-front">
        <div class="card-name">dorian welles<br>managing director</div>
        <div class="card-lines">Level 9 Harbour Court,<br>40 Quay Rd, Perth, WA 6000<br>PO Box 2284, Perth, WA 6831<br><br>m. 0407 218 936<br>e. dorian@marketlane.com.au<br>w. www.marketlane.com.au</div>
        <div class="card-brand"><span class="brand-square"></span>marketlane</div>
      </div>
      <div class="card-back">
        <div class="card-back-top">
          <div class="card-back-brand"><span class="brand-square"></span>marketlane</div>
          <div class="card-back-tag">local stores online</div>
        </div>
      </div>
    </section>

    <section class="sample-frame sample-logo" aria-label="Logo sample">
      <span class="client-name">BOLTWIRE ELECTRONIC ENGINEERS</span>
    </section>

    <p class="services">Our services include all aspects of graphic design from logo design, business stationery, ads, brochures, or even typesetting, Heron Graphics can cater to all your design requirements as well as printing needs. We will take you through from beginning to end, from creative brief solutions, to the final printed product. We’re here to make things easy for you and take your business to the next level.</p>

    <div class="brand">
      <div class="brand-name">heron graphics</div>
      <div class="brand-tag">communication by design</div>
    </div>

    <p class="contact">Phone (08) 7315 4097&nbsp;&nbsp;&nbsp;Email: heron.graphics@plovermail.net.au</p>

    <div class="promo-rule" style="top:666px"></div>
    <p class="promo">Mention this flyer and receive 20%<br>off all artwork and 10% off all printing</p>
    <div class="promo-rule" style="top:770px"></div>
  </main>
</div>
</body>
</html>
```